Business card for different employees

A professional new updated design incorporating our current business's color themes and styles such as our on-site service trucks decals included in pictures attached. Our current business card is very simple and not professionally designed. We are a small family business but want a professional corporate look.

Target Market(s)

Cards to be handed out to new customers , corperate meetings. For our on site service operators.

Industry/Entity Type

Hydraulic

Contact Information for Business Card

Address, website, phone number, email, logo.
slogan - "Industry chosen hose and fittings provider".
24/7 on-site service , supply and hose management
Experienced , indpendant , family owned

Font styles to use
Sans Serif

Requirements
Must have
• Easily editable so that I can add different names and different roles for employees etc.
Nice to have
• Freedom with colour doesn't necessarily have to be blue but that is our company colour theme with trucks and logo so makes sense for the card to have blue like the trucks.

```html
<!DOCTYPE html>
<html lang="en">
<head>
<meta charset="utf-8">
<title>Meridian Hose Supply – Business Card</title>
<link href="https://fonts.googleapis.com/css2?family=Open+Sans:wght@400;600;700;800&family=Michroma&family=Roboto+Condensed:wght@700&display=swap" rel="stylesheet">
<style>
  :root {
    --bg: #e4e4e4;
    --card-white: #ffffff;
    --brand-blue: #1230c0;
    --name-blue: #1a36c4;
    --band-black: #1b1b1b;
    --text-grey: #555555;
    --band-grey: #8a8a8a;
    --band-light: #c9c9c9;
    --steel-light: #e6e6e6;
    --steel-dark: #8c8c8c;
    --white: #ffffff;
  }
  * { margin: 0; padding: 0; box-sizing: border-box; }
  html, body { width: 1125px; height: 1200px; overflow: hidden; background: var(--bg); }
  body { position: relative; font-family: "Open Sans", Arial, sans-serif; }

  .card {
    position: absolute; left: 150px; width: 800px; height: 457px;
    border-radius: 26px; overflow: hidden;
    box-shadow: 0 4px 10px rgba(0,0,0,0.25);
  }
  .card--front { top: 95px; background: var(--card-white); }
  .card--back { top: 612px; background: var(--brand-blue); }

  /* brand lockup */
  .brand { position: absolute; display: flex; align-items: center; }
  .card--front .brand { left: 112px; top: 82px; gap: 22px; }
  .brand__dot { width: 118px; height: 118px; border-radius: 50%; background: var(--band-black); flex: none; }
  .brand__name {
    font-weight: 800; font-size: 27px; color: var(--name-blue);
    letter-spacing: 1px; text-transform: uppercase; line-height: 1; white-space: nowrap;
  }

  /* person + contact */
  .person { position: absolute; right: 446px; top: 252px; text-align: right; }
  .person__name { font-weight: 700; font-size: 26px; color: var(--name-blue); letter-spacing: 0.5px; }
  .person__role { font-size: 16px; color: #222; margin-top: 2px; }
  .divider { position: absolute; left: 380px; top: 236px; width: 1.5px; height: 90px; background: var(--name-blue); }
  .contact { position: absolute; left: 407px; top: 235px; font-size: 16.5px; color: var(--text-grey); line-height: 22px; }
  .contact__address { margin-bottom: 6px; }
  .contact__line { display: flex; align-items: center; gap: 6px; }
  .contact__line svg { width: 14px; height: 14px; fill: var(--name-blue); }

  /* bottom band */
  .band {
    position: absolute; left: 0; height: 32px; width: 675px; background: var(--band-black);
    display: flex; align-items: center; justify-content: center; white-space: nowrap;
    font-family: "Michroma", Arial, sans-serif;
  }
  .card--front .band { top: 394px; font-size: 16px; letter-spacing: 3px; }
  .card--back .band { top: 393px; font-size: 13px; letter-spacing: 2px; padding-left: 60px; }
  .band__web { color: var(--band-grey); }
  .band__web b { color: var(--band-light); font-weight: 400; }
  .fitting {
    position: absolute; left: 675px; width: 90px; height: 34px; border-radius: 3px;
    background: linear-gradient(180deg, var(--steel-dark), var(--steel-light) 45%, var(--steel-dark));
  }
  .card--front .fitting { top: 393px; }
  .card--back .fitting { top: 392px; }

  /* back */
  .card--back .brand__dot {
    position: absolute; left: 110px; top: 106px; width: 200px; height: 200px;
    background: #d8d8d8; display: flex; align-items: center; justify-content: center; text-align: center;
  }
  .card--back .brand__name { font-size: 22px; line-height: 1.15; }
  .services { position: absolute; left: 308px; top: 144px; width: 357px; }
  .services__item {
    height: 36px; margin-bottom: 9px; background: var(--band-black); white-space: nowrap;
    font-family: "Roboto Condensed", Arial, sans-serif; font-weight: 700; font-size: 19px;
    color: var(--white); display: flex; align-items: center; padding-left: 34px;
  }
  .services__item:nth-child(3) { margin-top: 12px; }
  .muted { color: var(--band-grey); }
  .slogan { color: var(--band-grey); }
  .slogan b { color: var(--band-light); font-weight: 400; }
</style>
</head>
<body>

<section class="card card--front">
  <div class="brand">
    <span class="brand__dot"></span>
    <span class="brand__name">Meridian Hose Supply</span>
  </div>

  <div class="person">
    <div class="person__name">DANIEL BROOKS</div>
    <div class="person__role">PRESIDENT</div>
  </div>
  <div class="divider"></div>
  <div class="contact">
    <div class="contact__address">412 Harbour Road<br>Eastfield, Alaska 34120</div>
    <div class="contact__line">
      <svg viewBox="0 0 24 24"><path d="M6.6 10.8a15 15 0 0 0 6.6 6.6l2.2-2.2c.3-.3.7-.4 1-.2 1.1.4 2.3.6 3.6.6.6 0 1 .4 1 1V20c0 .6-.4 1-1 1C10.6 21 3 13.4 3 4c0-.6.4-1 1-1h3.5c.6 0 1 .4 1 1 0 1.3.2 2.5.6 3.6.1.3 0 .7-.2 1z"/></svg>
      0400 555 219
    </div>
    <div class="contact__line">
      <svg viewBox="0 0 24 24"><path d="M2 5h20v14H2z M2 5l10 8 10-8" fill="none" stroke="var(--name-blue)" stroke-width="2.5"/></svg>
      info@meridianhose.com.au
    </div>
  </div>

  <div class="band"><span class="band__web">WWW.<b>MERIDIANHOSE</b>.COM.AU</span></div>
  <div class="fitting" role="img" aria-label="Steel hose fitting end"></div>
</section>

<section class="card card--back">
  <div class="brand__dot"><span class="brand__name">Meridian<br>Hose Supply</span></div>

  <div class="services">
    <div class="services__item"><span class="muted">24/7&nbsp;</span>On-Site Service</div>
    <div class="services__item"><span class="muted">Supply&nbsp;</span>&amp; Hose Management</div>
    <div class="services__item">Experienced | Independant&nbsp;<span class="muted">| Family owned</span></div>
  </div>

  <div class="band"><span class="slogan">INDUSTRY <b>CHOSEN HOSE &amp; FITTINGS</b> PROVIDER</span></div>
  <div class="fitting" role="img" aria-label="Steel hose fitting end"></div>
</section>

</body>
</html>
```